Redesign Comparisson chart - make modern and effective

Use your imaginations to make a powerful distinction between QVR & other holistic modalities. There are 7 elements physical, mental, emotional, energetic, subconscious, superconscious and before and after testing.
We want it to be obvious that QVR is the only modality that works on all these elements simultaneously. We do not want to include any chakras as we want this information to be accepted by a wide range of people and belief systems.'

We want it to look simple but effective. Professional but powerful. We want QVR to stand out even of you eye just passed over i.
Updates

Hi everyone, thanks for your submissions so far. Basically what this image is meant to represent is a comparison chart between all the modalities There are 5 elements physical, mental, emotional, subconscious and superconscious. we want to reflect that QVR is the only modality that works on all these elements simultaneously. As we want the concept to be accepted and not considered woo woo, we want to steer away from chakras.

Target Market(s)

Professionals

Industry/Entity Type

Professional services

Font styles to use
Sans Serif
Other font styles liked:
• Poppins Monserratt

Colors
0094D4
00A9DD
6FCCEA
C7EBF8
E9F6FB

Requirements
Must have
• Clear/professional and clean look. Brand colours and logos. All typography and formats must be cohesive.
Nice to have
• More easy to read, different layout
Should not have
• Do not change the data just the way its presented. No chakras

```html
<!DOCTYPE html>
<html lang="en">
<head>
<meta charset="utf-8">
<title>QVR – Modality Comparison Chart</title>
<link href="https://fonts.googleapis.com/css2?family=Poppins:ital,wght@0,400;0,500;0,600;0,700;1,600;1,700&display=swap" rel="stylesheet">
<style>
  :root{
    --brand:#2db8e8;
    --brand-light:#7dd9f5;
    --navy:#1d5470;
    --ink:#1b2533;
    --canvas:#eef3fb;
    --tube:#e1e4ec;
    --pink:#d672ad;
    --purple:#836bab;
    --yellow:#e8cf4e;
    --orange:#f29f36;
    --green:#5fae46;
    --blue:#63bedd;
    --red:#db4a40;
  }
  *{margin:0;padding:0;box-sizing:border-box}
  html,body{width:1200px;height:825px;overflow:hidden;background:#fff}
  body{font-family:'Poppins',sans-serif;color:var(--ink);position:relative}

  .header{position:absolute;left:0;top:0;width:1200px;height:109px;background:#fff}
  .headline{position:absolute;left:73px;top:34px;font-size:18.5px;line-height:23px;font-weight:600;color:var(--brand);letter-spacing:.2px}
  .brand-name{position:absolute;left:478px;top:42px;width:200px;text-align:center;font-size:17px;line-height:22px;font-weight:600;color:var(--brand);white-space:nowrap}
  .pledges{position:absolute;left:690px;top:33px;width:490px;text-align:center;font-size:8.3px;line-height:13.2px;font-weight:700;font-style:italic;color:var(--ink)}

  .stage{position:absolute;left:0;top:109px;width:1200px;height:716px;background:var(--canvas)}
  .chart{position:absolute;left:0;top:0;width:1200px;height:825px}

  .tube{fill:var(--tube)}
  .pink{fill:var(--pink)} .purple{fill:var(--purple)} .yellow{fill:var(--yellow)}
  .orange{fill:var(--orange)} .green{fill:var(--green)} .blue{fill:var(--blue)} .red{fill:var(--red)}
  .pin{fill:var(--navy)}
  .pin-line{stroke:var(--navy);stroke-width:1.2}
  .check{fill:var(--brand-light)}
  .seal{fill:var(--brand)}

  .tag{position:absolute;height:9.6px;background:var(--navy);color:#fff;border-radius:5px;font-size:8px;line-height:9.8px;padding:0 5px;white-space:nowrap;text-transform:uppercase}
  .tag.center{text-align:center}
  .tag.double{height:auto;line-height:8.4px;padding:2px 8px;border-radius:10px}

  .element{position:absolute;width:136px}
  .element h2{font-size:14.2px;line-height:17px;font-weight:600;text-transform:uppercase;letter-spacing:.2px}
  .element p{font-size:7.8px;line-height:9.6px;text-align:justify;color:var(--ink);margin-top:2px}
  .element.left{left:428px}
  .element.left h2{text-align:right}
  .element.right{left:636px}
  .t-pink{color:var(--pink)} .t-purple{color:var(--purple)} .t-yellow{color:var(--yellow)}
  .t-orange{color:var(--orange)} .t-green{color:var(--green)} .t-blue{color:var(--blue)} .t-red{color:var(--red)}

  .accent{stroke-width:1}
  .a-pink{stroke:var(--pink)} .a-purple{stroke:var(--purple)} .a-yellow{stroke:var(--yellow)}
  .a-orange{stroke:var(--orange)} .a-green{stroke:var(--green)} .a-blue{stroke:var(--blue)} .a-red{stroke:var(--red)}

  .footer{position:absolute;left:494px;top:788px;display:flex;align-items:center;gap:7px;color:var(--brand);font-size:12.5px;font-weight:600}
  .footer .dot{width:12px;height:12px;border-radius:50%;background:var(--brand)}
  .footer .divider{width:1px;height:14px;background:var(--brand)}
  .footer .site{font-size:11px;font-weight:500}
</style>
</head>
<body>

<header class="header">
  <h1 class="headline">CHOOSE QVR FOR FAST, IMMEDIATE AND<br>POWERFUL RESULTS</h1>
  <div class="brand-name">Quiet Vitality Reset</div>
  <p class="pledges">I MUST EXPERIENCE HEALING ON ALL LEVELS, I AM NOT JUST A BODY.<br>I WANT TO LEARN HOW TO HEAL MYSELF, SO I'M NOT DEPENDENT ON OTHERS.<br>I WANT TO RELEASE ALL MY EMOTIONAL AND MENTAL BLOCKS, SO I CAN BE THE BEST VERSION OF MYSELF.</p>
</header>

<div class="stage"></div>

<svg class="chart" viewBox="0 0 1200 825" aria-hidden="true">
  <!-- Left top group -->
  <g class="group">
    <rect class="tube" x="122" y="194" width="22" height="196" rx="11"/>
    <rect class="red" x="122" y="351.4" width="22" height="38.6" rx="11"/><rect class="red" x="122" y="351.4" width="22" height="19"/>
    <line class="pin-line" x1="133" y1="364" x2="133" y2="404"/><circle class="pin" cx="133" cy="364" r="2.6"/>

    <rect class="tube" x="185" y="194" width="22" height="196" rx="11"/>
    <rect class="red" x="185" y="351.4" width="22" height="38.6" rx="11"/><rect class="red" x="185" y="351.4" width="22" height="19"/>
    <rect class="blue" x="185" y="307.5" width="22" height="38.8"/>
    <line class="pin-line" x1="196" y1="167" x2="196" y2="208"/><circle class="pin" cx="196" cy="208" r="2.6"/>

    <rect class="tube" x="249" y="194" width="22" height="196" rx="11"/>
    <rect class="red" x="249" y="351.4" width="22" height="38.6" rx="11"/><rect class="red" x="249" y="351.4" width="22" height="19"/>
    <rect class="blue" x="249" y="307.5" width="22" height="38.8"/>
    <rect class="orange" x="249" y="263.6" width="22" height="38.8"/>
    <line class="pin-line" x1="260" y1="364" x2="260" y2="402"/><circle class="pin" cx="260" cy="364" r="2.6"/>

    <rect class="tube" x="313" y="194" width="22" height="196" rx="11"/>
    <rect class="red" x="313" y="351.4" width="22" height="38.6" rx="11"/><rect class="red" x="313" y="351.4" width="22" height="19"/>
    <rect class="orange" x="313" y="307.5" width="22" height="38.8"/>
    <line class="pin-line" x1="324" y1="167" x2="324" y2="208"/><circle class="pin" cx="324" cy="208" r="2.6"/>
  </g>

  <!-- Left bottom group -->
  <g class="group">
    <rect class="tube" x="122" y="531" width="22" height="196" rx="11"/>
    <rect class="red" x="122" y="688.4" width="22" height="38.6" rx="11"/><rect class="red" x="122" y="688.4" width="22" height="19"/>
    <rect class="pink" x="122" y="644.5" width="22" height="38.8"/>
    <line class="pin-line" x1="133" y1="701" x2="133" y2="741"/><circle class="pin" cx="133" cy="701" r="2.6"/>

    <rect class="tube" x="185" y="531" width="22" height="196" rx="11"/>
    <rect class="red" x="185" y="688.4" width="22" height="38.6" rx="11"/><rect class="red" x="185" y="688.4" width="22" height="19"/>
    <rect class="orange" x="185" y="644.5" width="22" height="38.8"/>
    <rect class="pink" x="185" y="600.6" width="22" height="38.8"/>
    <line class="pin-line" x1="196" y1="505" x2="196" y2="545"/><circle class="pin" cx="196" cy="545" r="2.6"/>

    <rect class="tube" x="249" y="531" width="22" height="196" rx="11"/>
    <rect class="red" x="249" y="688.4" width="22" height="38.6" rx="11"/><rect class="red" x="249" y="688.4" width="22" height="19"/>
    <rect class="yellow" x="249" y="644.5" width="22" height="38.8"/>
    <rect class="pink" x="249" y="600.6" width="22" height="38.8"/>
    <line class="pin-line" x1="260" y1="701" x2="260" y2="738"/><circle class="pin" cx="260" cy="701" r="2.6"/>

    <rect class="tube" x="313" y="531" width="22" height="196" rx="11"/>
    <rect class="red" x="313" y="688.4" width="22" height="38.6" rx="11"/><rect class="red" x="313" y="688.4" width="22" height="19"/>
    <rect class="blue" x="313" y="644.5" width="22" height="38.8"/>
    <rect class="yellow" x="313" y="600.6" width="22" height="38.8"/>
    <rect class="pink" x="313" y="556.7" width="22" height="38.8"/>
    <line class="pin-line" x1="324" y1="505" x2="324" y2="545"/><circle class="pin" cx="324" cy="545" r="2.6"/>
  </g>

  <!-- Right top group -->
  <g class="group">
    <rect class="tube" x="883" y="194" width="22" height="196" rx="11"/>
    <rect class="red" x="883" y="351.4" width="22" height="38.6" rx="11"/><rect class="red" x="883" y="351.4" width="22" height="19"/>
    <rect class="orange" x="883" y="307.5" width="22" height="38.8"/>
    <rect class="yellow" x="883" y="263.6" width="22" height="38.8"/>
    <rect class="pink" x="883" y="219.7" width="22" height="38.8"/>
    <line class="pin-line" x1="894" y1="364" x2="894" y2="404"/><circle class="pin" cx="894" cy="364" r="2.6"/>

    <rect class="tube" x="946" y="194" width="22" height="196" rx="11"/>
    <rect class="orange" x="946" y="351.4" width="22" height="38.6" rx="11"/><rect class="orange" x="946" y="351.4" width="22" height="19"/>
    <line class="pin-line" x1="957" y1="167" x2="957" y2="208"/><circle class="pin" cx="957" cy="208" r="2.6"/>

    <rect class="tube" x="1010" y="194" width="22" height="196" rx="11"/>
    <rect class="orange" x="1010" y="351.4" width="22" height="38.6" rx="11"/><rect class="orange" x="1010" y="351.4" width="22" height="19"/>
    <rect class="pink" x="1010" y="307.5" width="22" height="38.8"/>
    <line class="pin-line" x1="1021" y1="364" x2="1021" y2="400"/><circle class="pin" cx="1021" cy="364" r="2.6"/>

    <rect class="tube" x="1073" y="194" width="22" height="196" rx="11"/>
    <rect class="yellow" x="1073" y="351.4" width="22" height="38.6" rx="11"/><rect class="yellow" x="1073" y="351.4" width="22" height="19"/>
    <rect class="purple" x="1073" y="307.5" width="22" height="38.8"/>
    <line class="pin-line" x1="1084" y1="167" x2="1084" y2="208"/><circle class="pin" cx="1084" cy="208" r="2.6"/>
  </g>

  <!-- Right bottom group -->
  <g class="group">
    <rect class="tube" x="883" y="531" width="22" height="196" rx="11"/>
    <rect class="blue" x="883" y="688.4" width="22" height="38.6" rx="11"/><rect class="blue" x="883" y="688.4" width="22" height="19"/>
    <line class="pin-line" x1="894" y1="505" x2="894" y2="545"/><circle class="pin" cx="894" cy="545" r="2.6"/>

    <rect class="tube" x="946" y="531" width="22" height="196" rx="11"/>
    <rect class="blue" x="946" y="688.4" width="22" height="38.6" rx="11"/><rect class="blue" x="946" y="688.4" width="22" height="19"/>
    <rect class="pink" x="946" y="644.5" width="22" height="38.8"/>
    <line class="pin-line" x1="957" y1="701" x2="957" y2="739"/><circle class="pin" cx="957" cy="701" r="2.6"/>

    <rect class="tube" x="1010" y="531" width="22" height="196" rx="11"/>
    <rect class="blue" x="1010" y="688.4" width="22" height="38.6" rx="11"/><rect class="blue" x="1010" y="688.4" width="22" height="19"/>
    <rect class="yellow" x="1010" y="644.5" width="22" height="38.8"/>
    <line class="pin-line" x1="1021" y1="505" x2="1021" y2="545"/><circle class="pin" cx="1021" cy="545" r="2.6"/>

    <rect class="tube" x="1073" y="531" width="22" height="196" rx="11"/>
    <rect class="blue" x="1073" y="688.4" width="22" height="38.6" rx="11"/><rect class="blue" x="1073" y="688.4" width="22" height="19"/>
    <rect class="yellow" x="1073" y="644.5" width="22" height="38.8"/>
    <rect class="pink" x="1073" y="600.6" width="22" height="38.8"/>
    <line class="pin-line" x1="1084" y1="701" x2="1084" y2="741"/><circle class="pin" cx="1084" cy="701" r="2.6"/>
  </g>

  <!-- QVR central column -->
  <g class="qvr-column">
    <rect class="tube" x="588" y="131" width="26" height="110" rx="13"/>
    <rect class="pink" x="588" y="176" width="26" height="59" rx="4"/>
    <rect class="purple" x="588" y="241" width="26" height="68"/>
    <rect class="yellow" x="588" y="315" width="26" height="67"/>
    <rect class="orange" x="588" y="389" width="26" height="67"/>
    <rect class="green" x="588" y="462" width="26" height="68"/>
    <rect class="blue" x="588" y="535" width="26" height="68"/>
    <rect class="red" x="588" y="609" width="26" height="67" rx="13"/><rect class="red" x="588" y="609" width="26" height="40"/>
    <circle class="check" cx="601" cy="162" r="19"/>
    <path d="M592 162 l6 6 l11 -11" fill="none" stroke="#fff" stroke-width="4" stroke-linecap="round" stroke-linejoin="round"/>
    <line class="pin-line" x1="601" y1="652" x2="601" y2="700"/><circle class="pin" cx="601" cy="652" r="2.8"/>
    <circle class="seal" cx="601" cy="729" r="32"/>
  </g>

  <!-- Element connectors -->
  <g class="connectors">
    <line class="accent a-pink" x1="629" y1="168" x2="629" y2="233"/><line class="accent a-pink" x1="614" y1="196" x2="629" y2="196"/>
    <line class="accent a-purple" x1="570" y1="243" x2="570" y2="307"/><line class="accent a-purple" x1="570" y1="269" x2="588" y2="269"/>
    <line class="accent a-yellow" x1="629" y1="315" x2="629" y2="385"/><line class="accent a-yellow" x1="614" y1="341" x2="629" y2="341"/>
    <line class="accent a-orange" x1="570" y1="390" x2="570" y2="455"/><line class="accent a-orange" x1="570" y1="416" x2="588" y2="416"/>
    <line class="accent a-green" x1="629" y1="450" x2="629" y2="514"/><line class="accent a-green" x1="614" y1="489" x2="629" y2="489"/>
    <line class="accent a-blue" x1="570" y1="537" x2="570" y2="601"/><line class="accent a-blue" x1="570" y1="562" x2="588" y2="562"/>
    <line class="accent a-red" x1="629" y1="588" x2="629" y2="651"/><line class="accent a-red" x1="614" y1="631" x2="629" y2="631"/>
  </g>
</svg>

<!-- Modality labels: left -->
<div class="tag center" style="left:147px;top:158px;width:98px">Psychic Intuitive</div>
<div class="tag center" style="left:285px;top:158px;width:77px">Acupuncture</div>
<div class="tag" style="left:84px;top:404px;width:98px">Massage</div>
<div class="tag" style="left:84px;top:417px;width:98px">Yoga</div>
<div class="tag" style="left:84px;top:430px;width:98px">Natropathy</div>
<div class="tag" style="left:84px;top:443px;width:98px">Ayurvedic Medicine</div>
<div class="tag" style="left:84px;top:456px;width:98px">Western Medicine</div>
<div class="tag double" style="left:218px;top:401px;width:84px">Family<br>Constellation</div>

<div class="tag center" style="left:152px;top:495px;width:88px">Chinese Medicine</div>
<div class="tag center" style="left:308px;top:495px;width:30px">EFT</div>
<div class="tag" style="left:83px;top:741px;width:99px">Nutritional Healing</div>
<div class="tag" style="left:221px;top:738px;width:78px">Kinesiology</div>
<div class="tag" style="left:221px;top:751px;width:78px">Bowen Therapy</div>

<!-- Modality labels: right -->
<div class="tag" style="left:915px;top:145px;width:86px">Reiki</div>
<div class="tag" style="left:915px;top:158px;width:86px">Crystal Healing</div>
<div class="tag center" style="left:1044px;top:158px;width:80px">Theta Healing</div>
<div class="tag center" style="left:856px;top:404px;width:74px">Chiropractic</div>
<div class="tag center" style="left:979px;top:400px;width:85px">Energy Medicine</div>

<div class="tag center" style="left:856px;top:495px;width:78px">Pshychology</div>
<div class="tag" style="left:975px;top:483px;width:97px">Hypnotherapy</div>
<div class="tag" style="left:975px;top:496px;width:97px">Inner Child Healing</div>
<div class="tag double" style="left:918px;top:739px;width:84px">Mindfullness<br>Meditation</div>
<div class="tag" style="left:918px;top:763px;width:84px">Life Coaching</div>
<div class="tag" style="left:1042px;top:741px;width:90px">NLP</div>
<div class="tag" style="left:1042px;top:754px;width:90px">Timeline Theraphy</div>

<div class="tag center" style="left:544px;top:767px;width:114px">Quiet Vitality Reset</div>

<!-- Elements -->
<section class="element right" style="top:166px">
  <h2 class="t-pink">Before &amp; After<br>Testing</h2>
  <p>QVR is the only modality the enables you to provide before and after results, which are documented by us, and analysed by you with our help.</p>
</section>
<section class="element left" style="top:240px">
  <h2 class="t-purple">Superconscious</h2>
  <p>QVR is the only modality the enables you to access and heal your superconscious mind yourself.</p>
</section>
<section class="element right" style="top:312px">
  <h2 class="t-yellow">Subconscious</h2>
  <p>Some modalities, like Kinesiology, access your subconscious through muscle testing.<br>QVR empowers you to access your own subconscious and heal it yourself.</p>
</section>
<section class="element left" style="top:387px">
  <h2 class="t-orange">Energetic</h2>
  <p>Most modalities try to move the energy in your body for you. QVR enables and empowers you to do it yourself.</p>
</section>
<section class="element right" style="top:447px">
  <h2 class="t-green">Emotional</h2>
  <p>QVR is the only modality that engages your emotions on a physical level. Emotions get stuck in your body and can cause illness over time if left unchecked. QVR enables you you experience fast and powerful emotional releasing</p>
</section>
<section class="element left" style="top:534px">
  <h2 class="t-blue">Mental</h2>
  <p>QVR enables you to use your own consciousness to self-heal. We don't give you advice or coaching, we allow your mind to heal itself.</p>
</section>
<section class="element right" style="top:585px">
  <h2 class="t-red">Physical</h2>
  <p>Most modalities, including, a western medicine, focus on and treat the physical body only. The QVR process enables you to engage in healing your own body during the session. There is no muscle testing, no hands-on healing and no herbal remedies or medicines.</p>
</section>

<footer class="footer">
  <span class="dot"></span>
  <span class="name">lumenwell</span>
  <span class="divider"></span>
  <span class="site">www.lumenwell.com.au</span>
</footer>

</body>
</html>
```